Business Card Design

educational services
broker of essential services
So I love my The Copper Kettle cards. I love the background.
I like the background on the harbor crest card
I like a little part of each Meridel card
I want my card to stand out and be professional
I would also like somewhat of a brand
I do not want it to be specific to anything but the world and galaxy
I would like to be able to be used for everything, all encompassing
In spanish Sin fronteras, not sureother languages but i will do programs for other countries like China, Japan and Korea
Reason: It has been the first week of school and I have not been able to get the feedback I need.
Please change colors to Blue and GOld
Please add ~ over the n in Lucia
Please submit some vertical designs
Please include the world
Please make eagle a watermark
Make sure the Open Horizons doesnt have "learning academy" under it
I am open to new designs and I will pay more after I chose a designer who seems to get all this stuff in my head!
Reason: Last minute designs were wonderful
Reason: I was out of town and not able to review the wonderful designs posted. I am narrowing the designs down now! I appreciate all the work done thus far.
Hello,
Thank you for all the designs. This is difficult. I have not been able to access them as I was able to last week so please be patient. If you also do web design please send me a message.
Again, thank you. I am down to just a few designs.
Sincerely,
Lucia Ferrant Dowell
I have been extremely busy, I should pick a design by the ned of this week. Thank you for your patience
Industry/Entity Type
Business
Contact Information for Business Card
Dr. Lucia Ferrant Dowell
www.ohlearn.example
(555) 284-9063 US
luciaannferrant@mailbox.example
Look and feel

```html
<!DOCTYPE html>
<html lang="en">
<head>
<meta charset="utf-8">
<title>Dr. Lucia Ferrant Dowell – Business Card</title>
<link rel="stylesheet" href="https://fonts.googleapis.com/css2?family=Patrick+Hand&display=swap">
<style>
  :root {
    --bg-top: #2c2c2c;
    --bg-bottom: #222222;
    --band: #2f1f2c;
    --band-edge: #cfc9cd;
    --galaxy-violet: #8b5ec8;
    --galaxy-lilac: #b08ad8;
    --galaxy-blue: #5f66cf;
    --galaxy-deep: #2c1a3c;
    --galaxy-dark: #1e1526;
    --ink: #efe8f2;
  }
  html, body {
    margin: 0;
    padding: 0;
    width: 1200px;
    height: 702px;
    overflow: hidden;
    background: var(--bg-bottom);
  }
  .card {
    position: relative;
    width: 1200px;
    height: 702px;
    overflow: hidden;
    background: linear-gradient(180deg, var(--bg-top) 0%, var(--bg-bottom) 100%);
    font-family: "Patrick Hand", cursive;
    color: var(--ink);
  }
  .card-art {
    position: absolute;
    inset: 0;
    width: 1200px;
    height: 702px;
  }
  .contact-line {
    position: absolute;
    left: 77px;
    display: flex;
    align-items: center;
    gap: 14px;
    margin: 0;
    line-height: 1;
    white-space: nowrap;
  }
  .contact-name {
    top: 452px;
    font-size: 33px;
    letter-spacing: 2.5px;
  }
  .contact-phone {
    top: 503px;
    font-size: 36px;
    letter-spacing: 2.5px;
  }
  .contact-web {
    top: 553px;
    font-size: 33px;
    letter-spacing: 2px;
  }
  .contact-email {
    top: 604px;
    font-size: 32px;
    letter-spacing: 1.5px;
  }
  .contact-icon {
    width: 32px;
    height: 32px;
    flex: none;
  }
</style>
</head>
<body>
<div class="card">
  <svg class="card-art" viewBox="0 0 1200 702" xmlns="http://www.w3.org/2000/svg">
    <defs>
      <linearGradient id="galaxyTones" x1="0" y1="0" x2="1" y2="0.3">
        <stop offset="0" stop-color="var(--galaxy-deep)"/>
        <stop offset="0.14" stop-color="var(--galaxy-violet)"/>
        <stop offset="0.24" stop-color="var(--galaxy-lilac)"/>
        <stop offset="0.36" stop-color="var(--galaxy-dark)"/>
        <stop offset="0.5" stop-color="var(--galaxy-deep)"/>
        <stop offset="0.64" stop-color="var(--galaxy-violet)"/>
        <stop offset="0.76" stop-color="var(--galaxy-blue)"/>
        <stop offset="0.9" stop-color="var(--galaxy-deep)"/>
        <stop offset="1" stop-color="var(--galaxy-dark)"/>
      </linearGradient>
    </defs>
    <rect class="world-map" role="img"
          aria-label="World map of all continents filled with a purple and blue starry galaxy texture"
          x="166" y="50" width="930" height="515" rx="40" fill="url(#galaxyTones)" opacity="0.9"/>
    <path class="lower-band" d="M0,260 C360,420 760,565 1200,575 L1200,702 L0,702 Z" fill="var(--band)"/>
    <path class="band-edge" d="M0,260 C360,420 760,565 1200,575" fill="none" stroke="var(--band-edge)" stroke-width="2.5"/>
  </svg>

  <p class="contact-line contact-name">Dr. Lucia Ferrant Dowell</p>
  <p class="contact-line contact-phone">
    <svg class="contact-icon" viewBox="0 0 32 32" aria-hidden="true">
      <circle cx="16" cy="16" r="13.5" fill="none" stroke="currentColor" stroke-width="2.2"/>
      <path d="M11 9.5c1-.8 2-.6 2.5.3l1.3 2.3c.4.8.1 1.5-.6 2l-.8.6c.8 1.8 2 3 3.9 3.9l.6-.8c.5-.7 1.2-1 2-.6l2.3 1.3c.9.5 1.1 1.5.3 2.5-1.2 1.4-2.8 1.8-4.5 1.1-3.6-1.5-6.2-4.1-7.7-7.7-.7-1.7-.3-3.3 1.1-4.5z" fill="currentColor"/>
    </svg>
    <span>(555) 284-9063 US</span>
  </p>
  <p class="contact-line contact-web">
    <svg class="contact-icon" viewBox="0 0 32 32" aria-hidden="true">
      <circle cx="16" cy="16" r="13.5" fill="none" stroke="currentColor" stroke-width="2"/>
      <ellipse cx="16" cy="16" rx="6" ry="13.5" fill="none" stroke="currentColor" stroke-width="1.5"/>
      <line x1="2.5" y1="16" x2="29.5" y2="16" stroke="currentColor" stroke-width="1.5"/>
      <line x1="5" y1="9" x2="27" y2="9" stroke="currentColor" stroke-width="1.2"/>
      <line x1="5" y1="23" x2="27" y2="23" stroke="currentColor" stroke-width="1.2"/>
    </svg>
    <span>www.ohlearn.example</span>
  </p>
  <p class="contact-line contact-email">luciaannferrant@mailbox.example</p>
</div>
</body>
</html>
```